Bright, Fun and hard to forget home inspection business card.

We need a Business card design for a new Home Inspection company. We are building a brand that is bright, fun and easy to remember.

Target Market(s)

Anyone involed in buying and selling of homes.

Industry/Entity Type

Home Inspection

Contact Information for Business Card

Colin Marlowe Owner/Inspector

Wedsite- PorchAndRafterCheck.example
Phone: 253-555-0187
Email- ColinMarlowe@mailbox.example
WA Lic # 4806

Requirements
Must have
• BRQV LOGO somewhere on card.

```html
<!DOCTYPE html>
<html lang="en">
<head>
<meta charset="utf-8">
<title>Colin Marlowe – Porch And Rafter Check business card</title>
<link rel="stylesheet" href="https://fonts.googleapis.com/css2?family=Open+Sans:wght@700;800&display=swap">
<style>
  :root {
    --backdrop: #d8d3cb;
    --card: #f6f3ee;
    --brand-red: #c83a1c;
    --ink: #161616;
  }
  * { margin: 0; padding: 0; box-sizing: border-box; }
  html, body {
    width: 1200px; height: 970px; overflow: hidden;
    background: var(--backdrop);
    font-family: "Open Sans", Arial, sans-serif;
  }
  .card {
    position: absolute; left: 130px; top: 215px;
    width: 1000px; height: 570px;
    background: var(--card);
    box-shadow: 0 6px 24px rgba(0,0,0,.12);
  }
  .rule-vertical {
    position: absolute; left: 105px; top: 55px;
    width: 12px; height: 478px; background: var(--brand-red);
  }
  .rule-horizontal {
    position: absolute; left: 525px; top: 517px;
    width: 437px; height: 14px; background: var(--brand-red);
  }
  .person { position: absolute; left: 203px; top: 120px; text-align: center; width: 270px; }
  .person-name { color: var(--brand-red); font-size: 29px; font-weight: 700; line-height: 1.1; }
  .person-role { color: var(--ink); font-size: 18px; font-weight: 700; margin-top: 10px; }
  .contacts { position: absolute; left: 160px; top: 360px; list-style: none; }
  .contact-item {
    display: flex; align-items: center; gap: 14px;
    font-size: 18.5px; font-weight: 700; color: var(--ink);
    height: 48px;
  }
  .contact-icon { width: 32px; height: 26px; flex: none; }
  .brand {
    position: absolute; left: 565px; top: 100px;
    display: flex; align-items: center; gap: 18px;
  }
  .brand-dot { width: 86px; height: 86px; border-radius: 50%; background: var(--brand-red); flex: none; }
  .brand-name {
    color: var(--brand-red); font-weight: 800; font-size: 40px;
    line-height: 1.02; text-transform: uppercase;
  }
  .license {
    position: absolute; left: 798px; top: 293px;
    font-size: 17px; font-weight: 700; color: var(--ink);
  }
  .cert-badge { position: absolute; left: 880px; top: 428px; width: 80px; height: 82px; }
</style>
</head>
<body>
  <div class="card">
    <div class="rule-vertical"></div>
    <div class="rule-horizontal"></div>

    <div class="person">
      <h1 class="person-name">Colin Marlowe</h1>
      <p class="person-role">Owner/Inspector</p>
    </div>

    <ul class="contacts">
      <li class="contact-item">
        <svg class="contact-icon" viewBox="0 0 32 26" aria-hidden="true">
          <path fill="var(--brand-red)" d="M2 8c0-4 6-6 14-6s14 2 14 6v3h-7V8c-2-1-12-1-14 0v3H2z"/>
          <path fill="var(--brand-red)" d="M8 12h16l4 12H4z"/>
          <circle cx="16" cy="18" r="3" fill="var(--card)"/>
        </svg>
        253-555-0187
      </li>
      <li class="contact-item">
        <svg class="contact-icon" viewBox="0 0 32 26" aria-hidden="true">
          <rect x="2" y="4" width="28" height="18" fill="none" stroke="var(--brand-red)" stroke-width="2"/>
          <path d="M2 4l14 11L30 4M2 22l10-9M30 22l-10-9" fill="none" stroke="var(--brand-red)" stroke-width="2"/>
        </svg>
        ColinMarlowe@mailbox.example
      </li>
      <li class="contact-item">
        <svg class="contact-icon" viewBox="0 0 32 26" aria-hidden="true">
          <g fill="none" stroke="var(--brand-red)" stroke-width="2">
            <circle cx="16" cy="13" r="11"/>
            <ellipse cx="16" cy="13" rx="5" ry="11"/>
            <path d="M5 13h22M7 7h18M7 19h18"/>
          </g>
        </svg>
        www.porchandraftercheck.example
      </li>
    </ul>

    <div class="brand">
      <span class="brand-dot"></span>
      <p class="brand-name">Porch And<br>Rafter Check<br>LLC</p>
    </div>
    <p class="license">WA Lic # 4806</p>

    <svg class="cert-badge" viewBox="0 0 80 82" role="img" aria-label="BRQV certification badge">
      <rect x="0" y="0" width="80" height="82" fill="var(--ink)"/>
    </svg>
  </div>
</body>
</html>
```